Bramwell Exteriors Needs a New Website!

We are an exteriors company specializing in vinyl siding, Ardenwick siding, aluminum soffit/fascia, trough. We do new construction work as well as renovations. We also build detached garages.
You can view our current website at www.bramwellbuilders.ca
I want to completely overhaul the website.
Our services are different now as we no longer do new home construction as well as we do not do the snow clearing.
I want to focus on 2 things in particular on the website:

1/ Exterior renovations

2/ Detached Garage construction.

I have included our logo in the attached files to use as well.

Some features we would like:

1/ Be able to easily attach a video from Youtube/Vimeo to highlight a product or service
2/ Quick chat or contact button that we can talk to a potential client quickly
3/ Meet the Team page that is interesting and fresh
4/ Place for us to put in helpful exterior tips/suggestions for homeowners.

Content is not important, but looking for the best design that will attract people once they click on our page and want to renovate with us.

Target Market(s)

People looking for renovations on their home, people looking to build a detached garage.

Industry/Entity Type

Residential Construction

Coding

Coded - Design and coding required

Number of Pages Required

5+ page

Font styles to use
Sans Serif

Requirements
Must have
• Fresh and exciting home page.

Simple design. Don't want it over complicated or too much information to confuse the potential client.

Easy way to contact us.

Meet the team page that instills confidence
Nice to have
• Colour of website to go off our logo. Doesn't need to be an exact match, but something that goes well with our blue and grey.

```html
<!DOCTYPE html>
<html lang="en">
<head>
<meta charset="utf-8">
<title>Bramwell Exteriors</title>
<link href="https://fonts.googleapis.com/css2?family=Catamaran:wght@400;500;600;700;800&family=Lato:wght@400;700;900&display=swap" rel="stylesheet">
<style>
:root{
  --blue:#0d62b8;
  --blue-dark:#0a4e8e;
  --blue-light:#b8d7ee;
  --grey:#555a60;
  --grey-dark:#3a3d41;
  --text:#111;
  --muted:#6a6a6a;
  --panel:#f2f2f2;
  --contact-bg:#e2e2e2;
  --field:#f5f5f5;
  --footer:#050505;
  --white:#fff;
}
*{box-sizing:border-box;margin:0;padding:0}
html,body{width:1200px;height:4808px;overflow:hidden}
body{position:relative;background:var(--white);font-family:'Lato',sans-serif;color:var(--text)}
.abs{position:absolute}
h1,h2,h3,h4,.display{font-family:'Catamaran',sans-serif}

/* header */
.brand{display:flex;align-items:center;gap:10px;font-family:'Catamaran',sans-serif;font-weight:800;font-size:24px;color:var(--blue);letter-spacing:.5px;white-space:nowrap}
.brand-mark{width:42px;height:42px;border:4px solid currentColor;border-radius:50%}
.nav{left:557px;top:30px;display:flex;gap:33px;font-size:11px;color:#222}
.nav .active{color:var(--blue)}
.btn{background:var(--blue);color:#fff;font-family:'Catamaran',sans-serif;font-weight:700;display:flex;align-items:center;justify-content:center;border-radius:2px}

/* hero */
.hero-photo{left:293px;top:88px;width:907px;height:548px;background:linear-gradient(180deg,#4f8fd0 0%,#9fc4e6 38%,#b36a45 58%,#3b4f2e 78%,#2c2d2c 100%)}
.hero-side{left:30px;top:88px;height:552px;writing-mode:vertical-rl;transform:rotate(180deg);font-family:'Catamaran',sans-serif;font-weight:700;font-size:64px;color:#ececec;line-height:66px;white-space:nowrap;text-align:left}
.hero-box{left:157px;top:237px;width:338px;height:241px;background:var(--blue);color:#fff;padding:44px 24px 0}
.hero-box h1{font-size:56px;font-weight:500;line-height:1}
.hero-box h2{font-size:26px;font-weight:600;line-height:1.2;margin-top:4px;white-space:nowrap}
.hero-badge{margin-top:12px;width:274px;height:31px;background:#fff;color:#222;font-size:15px;display:flex;align-items:center;justify-content:center;gap:6px}
.hero-dots{left:709px;top:590px;display:flex;gap:14px;color:#fff;font-size:12px}
.hero-dots .on{color:var(--blue);font-weight:700;font-size:15px}

.tagline{left:0;top:700px;width:1200px;text-align:center;font-family:'Catamaran',sans-serif}
.tagline strong{display:block;font-size:32px;font-weight:700;line-height:42px}
.tagline span{display:block;font-size:30px;font-weight:400;line-height:40px}

/* services */
.svc-photo-l{left:0;top:939px;width:601px;height:569px;background:linear-gradient(180deg,#c9d1df 0%,#dfe4ec 30%,#3c3f52 55%,#262836 80%,#e7e9ef 100%)}
.svc-photo-r{left:601px;top:939px;width:599px;height:569px;background:linear-gradient(180deg,#3d74c4 0%,#a9c7e7 35%,#8a6c52 58%,#6d7b58 78%,#a3a7ad 100%)}
.svc-card{width:384px;height:347px;top:1088px;background:var(--blue-dark);padding:14px}
.svc-card .inner{border:2px solid #fff;height:100%;padding:30px 18px 0;color:#fff}
.svc-card h3{font-size:20px;font-weight:600;margin-bottom:14px}
.svc-card p{font-size:10.5px;line-height:18px}
.btn-white{margin-top:18px;width:100px;height:38px;background:#fff;color:#111;font-size:10px;font-weight:900;display:flex;align-items:center;justify-content:center;border-radius:3px}

/* section titles */
.sec-title{left:0;width:1200px;display:flex;align-items:center;justify-content:center;gap:30px;font-family:'Catamaran',sans-serif;font-weight:700;font-size:46px;color:#000}
.rule{width:118px;height:6px;border-top:2px solid var(--blue);border-bottom:1px solid var(--blue)}

/* why us */
.why-card{width:251px;height:163px;border:1.5px solid #a7c6e6;text-align:center;padding:28px 12px 0}
.why-card h4{color:var(--blue);font-size:16px;font-weight:700;margin-bottom:10px}
.why-card p{color:var(--muted);font-size:12.5px;line-height:20px}
.why-icon{position:absolute;left:50%;top:-38px;transform:translateX(-50%);width:76px;height:40px;overflow:hidden}
.why-icon .ring{width:76px;height:76px;border:2px solid var(--blue);border-radius:50%;background:#fff}
.why-icon svg{position:absolute;left:24px;top:8px}

/* video */
.video-photo{left:610px;top:2157px;width:590px;height:396px;background:linear-gradient(180deg,#4a64a8 0%,#a68fb2 35%,#e1b979 55%,#354b2e 80%,#24351f 100%)}
.play-main{left:638px;top:2212px;display:flex;align-items:center;gap:12px;color:#e8e8f6;font-size:15px}
.video-band{left:0;top:2469px;width:159px;height:84px;background:var(--blue-light)}
.video-title{left:157px;top:2196px;font-size:48px;font-weight:700}
.video-text{left:157px;top:2270px;width:404px;font-size:12px;line-height:19px;color:#444}
.thumb{top:2394px;width:276px;height:218px;background:#fff;box-shadow:0 2px 8px rgba(0,0,0,.15)}
.thumb.sel{border:2px solid var(--blue-dark)}
.thumb .img{height:152px}
.thumb .label{display:flex;align-items:center;gap:10px;padding:0 16px;height:64px;font-size:14px;font-weight:700}

/* team */
.team-bg{left:0;top:2687px;width:1200px;height:650px;background:var(--panel)}
.team-card{top:2848px;width:285px;height:365px;background:#fff;text-align:center}
.team-card .img{height:197px;background:linear-gradient(180deg,#8a8c52 0%,#b5aa6f 40%,#6f7b4a 100%)}
.team-card h4{font-family:'Lato',sans-serif;font-size:11.5px;font-weight:900;margin:23px 0 12px}
.team-card p{color:var(--muted);font-size:12.5px;line-height:20px;padding:0 28px}
.team-card a{display:block;color:var(--blue);font-size:12.5px;margin-top:18px;text-decoration:none}

/* testimonial */
.testi-card{left:157px;top:3486px;width:306px;height:298px;background:#fff;box-shadow:0 2px 10px rgba(0,0,0,.12);text-align:center;padding:18px 20px 0;font-size:13px;color:#222}
.testi-card .img{height:187px;background:linear-gradient(180deg,#5c7d3a 0%,#8fa35d 50%,#3f5527 100%);margin-bottom:10px}
.testi-line{left:463px;top:3500px;width:291px;height:2px;background:var(--blue)}
.testi-title{left:491px;top:3514px;font-size:50px;font-weight:600}
.testi-text{left:554px;top:3616px;width:490px;font-size:12.5px;line-height:20px;color:#444}
.quote{font-family:Georgia,serif;font-size:48px;font-weight:700;line-height:1}

/* contact */
.contact-bg{left:0;top:3893px;width:1200px;height:481px;background:var(--contact-bg)}
.field{background:var(--field);border:1px solid #d6d6d6;color:#888;font-size:13px;padding:14px 15px}

/* footer */
.footer{left:0;top:4374px;width:1200px;height:434px;background:var(--footer);color:#fff}
.footer h5{font-family:'Catamaran',sans-serif;font-size:16px;font-weight:700}
.footer p,.footer li,.footer td{font-size:10.5px;line-height:19px;color:#ddd}
.sitemap li{list-style:none;line-height:28px}
.sitemap li::before{content:"";display:inline-block;width:14px;height:1px;background:#ccc;margin-right:10px;vertical-align:middle}
.hours td{padding-right:18px;line-height:23.5px}
.contact-row{display:flex;gap:12px;align-items:flex-start;font-size:10.5px;color:#ddd;line-height:16px}
</style>
</head>
<body>

<!-- Header -->
<div class="abs brand" style="left:157px;top:16px"><span class="brand-mark"></span>Bramwell Exteriors</div>
<nav class="abs nav"><span class="active">Home</span><span>Service</span><span>Team</span><span>Testimonial</span><span>Contact Us</span></nav>
<div class="abs btn" style="left:946px;top:23px;width:96px;height:33px;font-size:11px">Get In Touch</div>

<!-- Hero -->
<div class="abs hero-side">Exteriors Company</div>
<div class="abs hero-photo" role="img" aria-label="Two-storey Tudor-style house with red roof under a blue sky"></div>
<div class="abs hero-box">
  <h1>Experience</h1>
  <h2>The Bramwell difference</h2>
  <div class="hero-badge"><svg width="14" height="14" viewBox="0 0 24 24"><path fill="#0d62b8" d="M12 2l3 7h7l-5.5 4.5 2 7.5L12 17l-6.5 4 2-7.5L2 9h7z"/></svg>Ardenwick siding</div>
</div>
<div class="abs hero-dots"><span class="on">01</span><span>02</span><span>03</span></div>

<div class="abs tagline"><strong>Honest and reliable construction service</strong><span>in Edmonton and area. We take pride in each and every project</span></div>
<div class="abs btn" style="left:496px;top:802px;width:185px;height:64px;font-size:21px">Get a Quote</div>

<!-- Services -->
<div class="abs svc-photo-l" role="img" aria-label="Dark-sided house in winter snow"></div>
<div class="abs svc-photo-r" role="img" aria-label="New home with detached garage and driveway"></div>
<div class="abs svc-card" style="left:157px"><div class="inner">
  <h3>Exterior renovations</h3>
  <p>Looking for a reputable company to replace those aging shingles? Wanting to update the look of your home to add more curb appeal? We can handle all your exterior renovation needs and would love an opportunity to speak with you about it. Contact us for a free, no obligation quote today. We also have the ability to help you design your new look and show it to you with our new partnership with HomeVista.</p>
  <div class="btn-white">Read More</div>
</div></div>
<div class="abs svc-card" style="left:672px"><div class="inner">
  <h3>Detached Garage construction</h3>
  <p>Lorem Ipsum is simply dummy text of the printing and typesetting industry. Lorem Ipsum has been the industry's standard dummy text ever since the 1500s, when an unknown printer took a galley of type and scrambled it to make a type specimen book. It has survived not only five centuries, but also the leap into electronic typesetting, remaining essentially unchanged.</p>
  <div class="btn-white">Read More</div>
</div></div>

<!-- Why Us -->
<div class="abs sec-title" style="top:1574px"><span class="rule"></span>Why Us<span class="rule"></span></div>

<div class="abs why-card" style="left:207px;top:1696px"><div class="why-icon"><div class="ring"></div><svg width="28" height="28" viewBox="0 0 24 24" fill="none" stroke="#111" stroke-width="2"><circle cx="12" cy="9" r="6" fill="#111"/><path d="M9 9l2 2 4-4" stroke="#fff"/><path d="M4 20h16"/></svg></div>
<h4>Certified experience</h4><p>Having professionals do the job gives you the confidence that the job will be done right, on budget, and on time.</p></div>
<div class="abs why-card" style="left:474px;top:1696px"><div class="why-icon"><div class="ring"></div><svg width="28" height="28" viewBox="0 0 24 24" fill="none" stroke="#111" stroke-width="1.5"><rect x="11" y="2" width="10" height="7" rx="1"/><circle cx="7" cy="13" r="3"/><circle cx="17" cy="13" r="3"/><path d="M2 22c0-3 2-5 5-5s5 2 5 5M12 22c0-3 2-5 5-5s5 2 5 5"/></svg></div>
<h4>Superior communication</h4><p>Taking the time to explain the construction process and promptly answering the phone or email is what sets us apart from others.</p></div>
<div class="abs why-card" style="left:741px;top:1696px"><div class="why-icon"><div class="ring"></div><svg width="28" height="28" viewBox="0 0 24 24" fill="none" stroke="#111" stroke-width="1.5"><circle cx="12" cy="12" r="9" stroke-dasharray="3 2"/><circle cx="12" cy="12" r="5"/><path d="M12 9v6M10 11h4"/></svg></div>
<h4>Competitive pricing</h4><p>Although we offer the best in services, we won't blow your budget on the job. We also take credit cards in our renovations division.</p></div>

<div class="abs why-card" style="left:207px;top:1920px"><div class="why-icon"><div class="ring"></div><svg width="28" height="28" viewBox="0 0 24 24" fill="none" stroke="#111" stroke-width="1.5"><rect x="7" y="4" width="15" height="9" rx="1"/><circle cx="14.5" cy="8.5" r="2"/><path d="M2 16l5-2 6 2 5-1-5 5-9-1z"/></svg></div>
<h4>Guaranteed satisfaction</h4><p>We aren't happy unless you are. Along with a robust limited lifetime warranty on our work, we ensure you are satisfied even years after completion.</p></div>
<div class="abs why-card" style="left:474px;top:1920px"><div class="why-icon"><div class="ring"></div><svg width="28" height="28" viewBox="0 0 24 24" fill="none" stroke="#111" stroke-width="1.5"><path d="M12 2l8 3v6c0 5-3.5 9-8 11-4.5-2-8-6-8-11V5z"/><circle cx="12" cy="12" r="4"/><rect x="10.5" y="11" width="3" height="3"/></svg></div>
<h4>Safety conscience</h4><p>COR certification, liability insurance, and WCB coverage on all workers gives you peace of mind that the job will be done safely.</p></div>
<div class="abs why-card" style="left:741px;top:1920px"><div class="why-icon"><div class="ring"></div><svg width="28" height="28" viewBox="0 0 24 24" fill="#111"><circle cx="12" cy="9" r="7"/><circle cx="12" cy="9" r="3" fill="#fff"/><path d="M7 14l-3 8 4-2 2 3 2-6zM17 14l3 8-4-2-2 3-2-6z"/></svg></div>
<h4>Unrivalled quality</h4><p>Our greatest asset is our unrivalled pursuit of a "top of the line" job each and every time.</p></div>

<!-- Video -->
<div class="abs video-photo" role="img" aria-label="Modern house lit up at dusk"></div>
<div class="abs play-main"><svg width="44" height="44" viewBox="0 0 44 44"><circle cx="22" cy="22" r="20" fill="none" stroke="#fff" stroke-width="2.5"/><path d="M17 13l13 9-13 9z" fill="var(--blue)"/></svg>Play Video</div>
<div class="abs video-band"></div>
<h2 class="abs video-title display">Video From</h2>
<p class="abs video-text">Lorem Ipsum is simply dummy text of the printing and typesetting industry. Lorem Ipsum has been the industry's standard dummy text ever since the 1500s, when an unknown printer took a galley of type and scrambled it to make a type specimen book.</p>

<div class="abs thumb" style="left:159px"><div class="img" role="img" aria-label="Brick bungalow with attached garage" style="background:linear-gradient(180deg,#3f7fcf 0%,#9cc2e8 45%,#b67a4f 70%,#cbbda3 100%)"></div>
<div class="label"><svg width="26" height="26" viewBox="0 0 26 26"><circle cx="13" cy="13" r="11" fill="none" stroke="#222" stroke-width="2"/><path d="M10 8l8 5-8 5z" fill="#222"/></svg>Video Play</div></div>
<div class="abs thumb sel" style="left:442px"><div class="img" role="img" aria-label="Contemporary home glowing at dusk" style="background:linear-gradient(180deg,#3b55a6 0%,#8d7fb0 40%,#d8b35e 62%,#2e3d21 100%)"></div>
<div class="label"><svg width="26" height="26" viewBox="0 0 26 26"><circle cx="13" cy="13" r="11" fill="none" stroke="#222" stroke-width="2"/><path d="M10 8l8 5-8 5z" fill="#222"/></svg>Video Play</div></div>
<div class="abs thumb" style="left:726px"><div class="img" role="img" aria-label="Two-storey house with brown siding" style="background:linear-gradient(180deg,#5b8fd6 0%,#a8c6ea 35%,#7b6652 60%,#5c6a43 100%)"></div>
<div class="label"><svg width="26" height="26" viewBox="0 0 26 26"><circle cx="13" cy="13" r="11" fill="none" stroke="#222" stroke-width="2"/><path d="M10 8l8 5-8 5z" fill="#222"/></svg>Video Play</div></div>

<!-- Team -->
<div class="abs team-bg"></div>
<div class="abs sec-title" style="top:2751px"><span class="rule"></span>Our Team<span class="rule"></span></div>
<div class="abs team-card" style="left:157px"><div class="img" role="img" aria-label="Portrait of the general manager in a field"></div>
<h4>Dale Morrow ~ General Manager</h4><p>Dale is the owner and General Manager of Bramwell Builders. He is principally focused on the building component</p><a>Read More</a></div>
<div class="abs team-card" style="left:457px"><div class="img" role="img" aria-label="Portrait of the operations manager in a field"></div>
<h4>Owen Pryce ~ Operations Manager (Exteriors)</h4><p>Owen started with Bramwell as a delivery driver around two and a half years ago. Since then, he has transitioned</p><a>Read More</a></div>
<div class="abs team-card" style="left:758px"><div class="img" role="img" aria-label="Portrait of the field service manager in a field"></div>
<h4>Elias Vandermeer ~ Field Service Manager</h4><p>Elias oversees the contracting division for Bramwell which includes snow clearing for the winter season.</p><a>Read More</a></div>
<div class="abs btn" style="left:549px;top:3226px;width:100px;height:36px;font-size:10px">View All</div>

<!-- Testimonial -->
<div class="abs testi-card"><div class="img" role="img" aria-label="Smiling senior couple outdoors"></div>Home owner<br>Jhon Doe</div>
<div class="abs testi-line"></div>
<h2 class="abs testi-title display">Testimonial</h2>
<div class="abs quote" style="left:535px;top:3580px">&ldquo;</div>
<p class="abs testi-text">Lorem Ipsum is simply dummy text of the printing and typesetting industry. Lorem Ipsum has been the industry's standard dummy text ever since the 1500s, when an unknown printer took a galley of type and scrambled it to make a type specimen book. It has survived not only five centuries, but also the leap into electronic typesetting, remaining essentially unchanged.</p>
<div class="abs" style="left:557px;top:3730px;font-size:14px;font-weight:700">Home owner<div style="font-size:12px;font-weight:400;color:#444">Jhon Doe</div></div>
<div class="abs quote" style="left:895px;top:3722px">&rdquo;</div>
<div class="abs" style="left:726px;top:3748px;display:flex;gap:6px"><span style="width:10px;height:10px;border-radius:50%;background:var(--blue)"></span><span style="width:10px;height:10px;border-radius:50%;background:#ddd"></span><span style="width:10px;height:10px;border-radius:50%;background:#ddd"></span></div>

<!-- Contact -->
<div class="abs contact-bg"></div>
<div class="abs sec-title" style="top:3961px"><span class="rule"></span>Contact Us<span class="rule"></span></div>
<div class="abs field" style="left:157px;top:4044px;width:435px;height:48px">Name</div>
<div class="abs field" style="left:595px;top:4044px;width:446px;height:48px">Email</div>
<div class="abs field" style="left:157px;top:4096px;width:435px;height:48px">Phone</div>
<div class="abs field" style="left:595px;top:4096px;width:446px;height:48px">Choose a Subject</div>
<div class="abs field" style="left:157px;top:4150px;width:884px;height:93px">Message</div>
<div class="abs btn" style="left:534px;top:4253px;width:130px;height:48px;font-size:15px">Send Message</div>

<!-- Footer -->
<footer class="abs footer">
  <div class="abs brand" style="left:157px;top:80px;color:#fff;font-size:22px"><span class="brand-mark" style="width:38px;height:38px"></span>Bramwell Exteriors</div>
  <p class="abs" style="left:157px;top:136px;width:215px">Looking for a reputable company to replace those aging shingles? Wanting to update the look of your home to add more curb appeal? We can handle all your exterior renovation needs and would love an opportunity to speak with you about it.</p>
  <h5 class="abs" style="left:157px;top:276px">Service region</h5>
  <p class="abs" style="left:157px;top:300px">Edmonton and Area</p>

  <h5 class="abs" style="left:411px;top:92px">Sitemap</h5>
  <ul class="abs sitemap" style="left:411px;top:130px"><li>Home</li><li>Service</li><li>Team</li><li>Testimonial</li><li>Contact Us</li></ul>

  <h5 class="abs" style="left:560px;top:92px">Opening Time</h5>
  <table class="abs hours" style="left:560px;top:132px;border-collapse:collapse">
    <tr><td>Monday</td><td>8:00 AM&nbsp; - &nbsp;4:30 PM</td></tr>
    <tr><td>tuesday</td><td>8:00 AM&nbsp; - &nbsp;4:30 PM</td></tr>
    <tr><td>Wednesday</td><td>8:00 AM&nbsp; - &nbsp;4:30 PM</td></tr>
    <tr><td>Thesday</td><td>8:00 AM&nbsp; - &nbsp;4:30 PM</td></tr>
    <tr><td>Friday</td><td>8:00 AM&nbsp; - &nbsp;4:30 PM</td></tr>
    <tr><td>Saturday</td><td>Closed</td></tr>
    <tr><td>Sunday</td><td>Closed</td></tr>
  </table>

  <h5 class="abs" style="left:821px;top:92px">Contact Us</h5>
  <div class="abs contact-row" style="left:821px;top:136px;width:230px"><svg width="12" height="14" viewBox="0 0 24 28"><path fill="#fff" d="M12 0a10 10 0 0 0-10 10c0 8 10 18 10 18s10-10 10-18A10 10 0 0 0 12 0zm0 14a4 4 0 1 1 0-8 4 4 0 0 1 0 8z"/></svg><span>118-40210 RR 214 Ashford Park, AB<br>T0X 2M4</span></div>
  <div class="abs contact-row" style="left:821px;top:190px"><svg width="14" height="14" viewBox="0 0 24 24"><path fill="#fff" d="M6.6 10.8a15 15 0 0 0 6.6 6.6l2.2-2.2a1 1 0 0 1 1-.25 11.4 11.4 0 0 0 3.6.57 1 1 0 0 1 1 1V20a1 1 0 0 1-1 1A17 17 0 0 1 3 4a1 1 0 0 1 1-1h3.5a1 1 0 0 1 1 1c0 1.25.2 2.450.57 3.6a1 1 0 0 1-.25 1z"/></svg><span>780-555-0142</span></div>
  <div class="abs contact-row" style="left:821px;top:222px"><svg width="14" height="12" viewBox="0 0 24 18" fill="none" stroke="#fff" stroke-width="2"><rect x="1" y="1" width="22" height="16"/><path d="M1 1l11 9 11-9"/></svg><span>info@bramwellbuilders.ca</span></div>
  <h5 class="abs" style="left:821px;top:256px">Bramwell Builders</h5>
  <p class="abs" style="left:821px;top:280px;font-size:10px">Ashford Park, Alberta</p>

  <p class="abs" style="left:0;top:404px;width:1200px;text-align:center;font-size:9.5px">©2020 BRAMWELL EXTERIORS.All rights reserved</p>
</footer>

</body>
</html>
```